Marlowe Tindra Pale Ale Beer Label/Badge

We need a Beer Label designed for our first official beer to be launched under The marlowe Brand!!
It will be a Pale Ale Called "Tindra Pale Ale"!

The Marlowe has the largest Craft Beer & Cider selection in the Geelong & Surf Coast region. With a funky location and a relaxed vibe, Marlowe prides itself on serving delicious, unique seasonal food paired with Australia's best Craft Beer. The marlowe is the perfect setting for a relaxed afternoon or evening with friends and can package an experience for larger groups or corporate bookings.

The Marlowe Tavern brand has been growing for over a year and a half and the first label needs to integrate The marlowe Logo but at the same time bring a fresh, new and eye catching feel to it along with embracing the "Odysseus" story in which we will be naming future beers.

The story of Tindra is found via the following link
http://en.lorevault.example/wiki/Tindra_(legend)

We expect designers to research The marlowe Tavern brand along with the all important Craft Beer Market and demographics. This will, potentially, be the start of many more labels to come for the winning designer!!

Requirements
Must have
• The original "O" needs to be integrated into the new logo and as much as the Greek mythology is being used it needs to be certain that this is an original Australian Craft Beer in the modern age!!
strong, modern & unique!!
Nice to have
• Logo could have a depiction of Tindra
Should not have
• tackiness or cheap!!

```html
<!DOCTYPE html>
<html lang="en">
<head>
<meta charset="utf-8">
<title>Tindra Pale Ale – Label</title>
<link href="https://fonts.googleapis.com/css2?family=Berkshire+Swash&family=Oleo+Script:wght@700&family=Pirata+One&display=swap" rel="stylesheet">
<style>
  :root {
    --paper: #ffffff;
    --foam-light: #efe6cf;
    --foam-mid: #ddd0ad;
    --beer-top: #f2c23a;
    --beer-deep: #d98c0c;
    --sky-deep: #1c5fb8;
    --sky-pale: #dcecf4;
    --horizon-white: #f7f9f6;
    --band-dark: #3a2612;
    --amber: #d8931f;
    --cream: #f6e7b8;
    --title-red: #8c1d28;
    --outline-white: #ffffff;
    --script-ink: #141010;
    --brand-ink: #4a1422;
  }
  html, body {
    margin: 0;
    padding: 0;
    width: 1200px;
    height: 922px;
    overflow: hidden;
    background: var(--paper);
  }
  .canvas {
    display: block;
    width: 1200px;
    height: 922px;
  }
  .label-title {
    font-family: "Berkshire Swash", "Georgia", serif;
    font-size: 56px;
    fill: var(--title-red);
    stroke: var(--outline-white);
    stroke-width: 3px;
    paint-order: stroke fill;
  }
  .label-tagline {
    font-family: "Pirata One", "Times New Roman", serif;
    font-size: 32px;
    fill: var(--script-ink);
    stroke: var(--outline-white);
    stroke-width: 3px;
    paint-order: stroke fill;
    letter-spacing: 1px;
  }
  .brand-name {
    font-family: "Berkshire Swash", "Georgia", serif;
    font-size: 44px;
    fill: var(--brand-ink);
  }
  .brand-dot { fill: var(--brand-ink); }
</style>
</head>
<body>
<svg class="canvas" viewBox="0 0 1200 922" xmlns="http://www.w3.org/2000/svg">
  <defs>
    <linearGradient id="foam" x1="0" y1="0" x2="0" y2="1">
      <stop offset="0" stop-color="var(--foam-light)"/>
      <stop offset="1" stop-color="var(--foam-mid)"/>
    </linearGradient>
    <linearGradient id="beer" x1="0" y1="0" x2="0" y2="1">
      <stop offset="0" stop-color="var(--beer-top)"/>
      <stop offset="1" stop-color="var(--beer-deep)"/>
    </linearGradient>
    <linearGradient id="badgeFill" x1="0" y1="234" x2="0" y2="668" gradientUnits="userSpaceOnUse">
      <stop offset="0" stop-color="var(--sky-deep)"/>
      <stop offset="0.22" stop-color="#5fa6dc"/>
      <stop offset="0.40" stop-color="var(--sky-pale)"/>
      <stop offset="0.50" stop-color="var(--horizon-white)"/>
      <stop offset="0.56" stop-color="#b8a67c"/>
      <stop offset="0.62" stop-color="var(--band-dark)"/>
      <stop offset="0.70" stop-color="var(--amber)"/>
      <stop offset="0.84" stop-color="#efc45e"/>
      <stop offset="1" stop-color="var(--cream)"/>
    </linearGradient>
    <linearGradient id="badgeEdge" x1="0" y1="0" x2="1" y2="0">
      <stop offset="0" stop-color="#000" stop-opacity="0.35"/>
      <stop offset="0.12" stop-color="#000" stop-opacity="0"/>
      <stop offset="0.88" stop-color="#000" stop-opacity="0"/>
      <stop offset="1" stop-color="#000" stop-opacity="0.35"/>
    </linearGradient>
    <filter id="badgeShadow" x="-10%" y="-10%" width="120%" height="130%">
      <feDropShadow dx="0" dy="6" stdDeviation="6" flood-color="#5a4520" flood-opacity="0.45"/>
    </filter>
  </defs>

  <rect class="top-margin" x="0" y="0" width="1200" height="24" fill="var(--paper)"/>
  <rect class="foam-area" x="0" y="24" width="1200" height="698" fill="url(#foam)"
        role="img" aria-label="Close-up photograph of beer foam bubbles"/>
  <rect class="beer-area" x="0" y="722" width="1200" height="200" fill="url(#beer)"
        role="img" aria-label="Photograph of golden beer with condensation droplets"/>

  <g class="badge" filter="url(#badgeShadow)">
    <path class="badge-shape"
          d="M324 238 Q612 266 906 244 Q922 250 926 262 Q932 444 912 612 Q906 636 880 640 Q612 676 340 640 Q316 636 312 612 Q292 444 298 262 Q302 242 324 238 Z"
          fill="url(#badgeFill)" stroke="#c9bfa4" stroke-width="2"/>
    <path d="M324 238 Q612 266 906 244 Q922 250 926 262 Q932 444 912 612 Q906 636 880 640 Q612 676 340 640 Q316 636 312 612 Q292 444 298 262 Q302 242 324 238 Z"
          fill="url(#badgeEdge)"/>
  </g>

  <g class="brand-mark">
    <circle class="brand-dot" cx="510" cy="370" r="12"/>
    <text class="brand-name" x="625" y="386" text-anchor="middle">Marlowe</text>
  </g>

  <text class="label-title" x="618" y="558" text-anchor="middle">Tindra Pale Ale</text>
  <text class="label-tagline" x="610" y="633" text-anchor="middle">Craft Beer &amp; Cider</text>
</svg>
</body>
</html>
```